Business Card Design Project

Basic business card with minimal details. I just need company name, email & web address, telephone and my name.
I would like the back of the card to be grey with my logo & company name centred.

Target Market(s)

Architects
Builders
Property Developers

Industry/Entity Type

Business

Font styles to use
Sans Serif

Colors

Designer to choose colors to be used in the design.

Requirements
Must have
• Venture Frame
Marcus Hadley - Director
M: 0452 913084
E: marcus@ventureframe.com.au
W: www.ventureframe.com.au
Should not have
• No other images or pictures

```html
<!DOCTYPE html>
<html lang="en">
<head>
<meta charset="utf-8">
<title>Venture Frame — Business Card</title>
<link rel="stylesheet" href="https://fonts.googleapis.com/css2?family=Montserrat:wght@400;500;600&display=swap">
<style>
  :root {
    --backdrop: #c9cacc;
    --card-slate: #51626f;
    --ink-white: #ffffff;
    --accent-red: #a6002c;
    --card-shadow: rgba(0, 0, 0, 0.28);
  }
  * { box-sizing: border-box; margin: 0; padding: 0; }
  html, body {
    width: 1200px;
    height: 1000px;
    overflow: hidden;
  }
  body {
    background: var(--backdrop);
    font-family: "Montserrat", Arial, sans-serif;
    position: relative;
  }
  .card {
    position: absolute;
    width: 610px;
    height: 265px;
    background: var(--card-slate);
    box-shadow: 0 4px 10px var(--card-shadow);
    overflow: hidden;
  }
  .card--front { left: 295px; top: 95px; }
  .card--back  { left: 295px; top: 525px; }

  /* Front */
  .brand-block {
    position: absolute;
    left: 26px;
    top: 100px;
    display: flex;
    align-items: center;
    gap: 12px;
  }
  .brand-block__square {
    width: 22px;
    height: 22px;
    background: var(--ink-white);
  }
  .brand-block__name {
    color: var(--ink-white);
    font-size: 22px;
    font-weight: 500;
    letter-spacing: 0.04em;
    text-transform: uppercase;
  }
  .person {
    position: absolute;
    left: 308px;
    top: 38px;
    color: var(--ink-white);
  }
  .person__name {
    font-size: 16px;
    font-weight: 500;
    letter-spacing: 0.01em;
  }
  .person__role {
    font-size: 11px;
    font-weight: 400;
    margin-top: 1px;
  }
  .contact {
    position: absolute;
    left: 308px;
    top: 172px;
    list-style: none;
    color: var(--ink-white);
    font-size: 13.5px;
    font-weight: 400;
  }
  .contact__row {
    display: flex;
    line-height: 21px;
  }
  .contact__label {
    width: 24px;
    color: var(--accent-red);
    font-weight: 500;
  }

  /* Back */
  .back-brand {
    position: absolute;
    right: 62px;
    bottom: 48px;
    display: flex;
    align-items: center;
    gap: 14px;
  }
  .back-brand__square {
    width: 26px;
    height: 26px;
    background: var(--accent-red);
  }
  .back-brand__name {
    color: var(--ink-white);
    font-size: 30px;
    font-weight: 500;
    letter-spacing: 0.05em;
    text-transform: uppercase;
  }
</style>
</head>
<body>
  <section class="card card--front" aria-label="Card front">
    <div class="brand-block">
      <span class="brand-block__square"></span>
      <span class="brand-block__name">Venture Frame</span>
    </div>
    <div class="person">
      <p class="person__name">Marcus Hadley</p>
      <p class="person__role">Director</p>
    </div>
    <ul class="contact">
      <li class="contact__row"><span class="contact__label">M</span><span>0452 913084</span></li>
      <li class="contact__row"><span class="contact__label">E</span><span>marcus@ventureframe.com.au</span></li>
      <li class="contact__row"><span class="contact__label">W</span><span>www.ventureframe.com.au</span></li>
    </ul>
  </section>

  <section class="card card--back" aria-label="Card back">
    <div class="back-brand">
      <span class="back-brand__square"></span>
      <span class="back-brand__name">Venture Frame</span>
    </div>
  </section>
</body>
</html>
```